Stationery for a private security company, "Tavrel Security Services Ltd."

Needed is a stationery design for a private security company. The designs must show professionalism and that our company mean nothing but business. Watermark of the company logo on the letterhead page is also a must. The final design must represent innovation and professionalism. It would be great if designers could integrate the colours black and silver onto the cards and letterheads..

Thank you

```html
<!DOCTYPE html>
<html lang="en">
<head>
<meta charset="utf-8">
<title>Tavrel Security Services Ltd. — Stationery</title>
<link href="https://fonts.googleapis.com/css2?family=Arimo:wght@400;700&display=swap" rel="stylesheet">
<style>
:root{
  --stage:#6b4a31;
  --paper:#ffffff;
  --ink:#1a1a1a;
  --silver:#b8c3c6;
  --silver-soft:#d9dddf;
  --mark-faint:#eeeeee;
  --label:#ffffff;
}
*{box-sizing:border-box;margin:0;padding:0}
html,body{width:1200px;height:515px;overflow:hidden}
body{background:var(--stage);font-family:"Arimo",Arial,sans-serif;color:var(--ink);position:relative}
.sheet,.envelope,.card{position:absolute;background:var(--paper);overflow:hidden}
.brand{position:absolute;font-weight:700;color:var(--ink);text-transform:uppercase;letter-spacing:.02em;line-height:1.1;display:flex;align-items:center;gap:4px}
.brand .dot{width:10px;height:10px;border-radius:50%;background:var(--silver);flex:none}
.brand-text{display:block}
.watermark{position:absolute;border-radius:50%;background:var(--mark-faint);display:flex;align-items:center;justify-content:center;text-align:center;font-weight:700;text-transform:uppercase;color:#e3e3e3;line-height:1.15}
.band{position:absolute;left:0;right:0;bottom:0;height:8px}
.small{font-size:6.4px;line-height:1.45}
.icon{width:6px;height:6px;vertical-align:-1px;margin-right:2px}
.contact-list{position:absolute;list-style:none;border-left:1px solid var(--ink);padding-left:4px}
.address{position:absolute}
/* letterhead */
.letterhead{left:16px;top:20px;width:342px;height:444px}
.fax{left:372px;top:20px;width:342px;height:444px}
.fax-title{position:absolute;left:22px;top:106px;font-size:24px;font-weight:400}
.fields{position:absolute;left:22px;top:145px;width:292px;display:grid;grid-template-columns:165px 118px;column-gap:9px;row-gap:9px;font-size:6.4px}
.field{border-bottom:1px solid var(--ink);height:10px}
.checks{position:absolute;left:22px;top:230px;display:flex;gap:11px;font-size:6.4px}
.checks span::before{content:"";display:inline-block;width:7px;height:7px;border:1px solid var(--ink);margin-right:4px;vertical-align:-1px}
.fax-footer{position:absolute;left:6px;bottom:14px;font-size:6.4px;display:flex;gap:8px;white-space:nowrap}
/* envelopes */
.env-back{left:788px;top:22px;width:384px;height:171px}
.env-black{left:776px;top:98px;width:384px;height:96px;background:#f1f1f1}
.env-front{left:750px;top:183px;width:362px;height:171px}
/* cards */
.card{width:142px;height:80px}
.card-a{left:730px;top:382px}
.card-b{left:880px;top:383px}
.card-c{left:1028px;top:382px}
.option{position:absolute;top:478px;font-size:22px;color:var(--label)}
</style>
</head>
<body>
<svg width="0" height="0" style="position:absolute" aria-hidden="true">
  <symbol id="i-phone" viewBox="0 0 10 10"><circle cx="5" cy="5" r="5" fill="#1a1a1a"/><path d="M3 2.5l1 1-.6.8a4 4 0 0 0 2.3 2.3l.8-.6 1 1-.8.9C4.8 7.7 2.3 5.2 2.1 3.3z" fill="#fff"/></symbol>
  <symbol id="i-mail" viewBox="0 0 10 10"><rect x="0" y="2" width="10" height="6.5" fill="#1a1a1a"/><path d="M.5 2.5 5 6l4.5-3.5" stroke="#fff" stroke-width=".8" fill="none"/></symbol>
  <symbol id="i-web" viewBox="0 0 10 10"><circle cx="5" cy="5" r="5" fill="#1a1a1a"/><path d="M0 5h10M5 0c-2.5 3-2.5 7 0 10M5 0c2.5 3 2.5 7 0 10" stroke="#fff" stroke-width=".6" fill="none"/></symbol>
  <symbol id="band" viewBox="0 0 100 8" preserveAspectRatio="none"><rect width="100" height="8" fill="#b8c3c6"/><path d="M58 8 64 2H100V8z" fill="#1a1a1a"/><path d="M58 8 64 2" stroke="#fff" stroke-width=".6"/></symbol>
</svg>

<!-- Letterhead -->
<section class="sheet letterhead" aria-label="Letterhead">
  <div class="brand" style="left:12px;top:14px;font-size:9px"><span class="dot"></span><span class="brand-text">Tavrel<br><span style="font-size:5px">Security Services Ltd.</span></span></div>
  <ul class="contact-list small" style="left:228px;top:16px">
    <li><svg class="icon"><use href="#i-phone"/></svg>555-310-4821</li>
    <li><svg class="icon"><use href="#i-phone"/></svg>555-310-4867</li>
    <li><svg class="icon"><use href="#i-mail"/></svg>info@tavrelsecurity.com</li>
    <li><svg class="icon"><use href="#i-web"/></svg>www.tavrelsecurity.com</li>
  </ul>
  <div class="watermark" role="img" aria-label="Faint company mark watermark" style="left:60px;top:130px;width:210px;height:210px;font-size:16px">Tavrel<br>Security</div>
  <p class="address" style="left:0;right:0;top:423px;text-align:center;font-size:7px;letter-spacing:.04em">Street Name, City Name State Zipcode</p>
  <svg class="band" viewBox="0 0 100 8" preserveAspectRatio="none" style="width:100%"><use href="#band"/></svg>
</section>

<!-- Fax sheet -->
<section class="sheet fax" aria-label="Fax cover sheet">
  <div class="brand" style="left:12px;top:14px;font-size:9px"><span class="dot"></span><span class="brand-text">Tavrel<br><span style="font-size:5px">Security Services Ltd.</span></span></div>
  <p class="address" style="left:250px;top:41px;font-size:7px;line-height:1.3">Street Name, City Name<br>State Zipcode</p>
  <h1 class="fax-title">FAX</h1>
  <div class="watermark" role="img" aria-label="Faint company mark watermark" style="left:60px;top:215px;width:200px;height:200px;font-size:16px">Tavrel<br>Security</div>
  <div class="fields">
    <div class="field">To :</div><div class="field">From :</div>
    <div class="field">Fax :</div><div class="field">Pages :</div>
    <div class="field">Phone :</div><div class="field">Date :</div>
    <div class="field">Re :</div><div class="field">CC :</div>
  </div>
  <div class="checks"><span>Urgent</span><span>For Review</span><span>Please Comment</span><span>Please Reply</span><span>Please Recycle</span></div>
  <p class="fax-footer">
    <span><svg class="icon"><use href="#i-phone"/></svg>555-310-4821</span>
    <span><svg class="icon"><use href="#i-phone"/></svg>555-310-4867</span>
    <span><svg class="icon"><use href="#i-mail"/></svg>info@tavrelsecurity.com</span>
    <span><svg class="icon"><use href="#i-web"/></svg>www.tavrelsecurity.com</span>
  </p>
</section>

<!-- Envelopes -->
<section class="envelope env-back" aria-label="Envelope back, silver flap">
  <svg width="384" height="171" style="position:absolute;left:0;top:0"><path d="M0 0H384V20Q384 30 370 34L205 72Q192 75 179 72L14 34Q0 30 0 20Z" fill="var(--silver)"/><circle cx="192" cy="48" r="16" fill="#a9b4b7"/></svg>
</section>
<section class="envelope env-black" aria-label="Envelope back, black flap">
  <svg width="384" height="96" style="position:absolute;left:0;top:0"><path d="M0 0H384V10Q384 22 368 26L205 66Q192 69 179 66L16 26Q0 22 0 10Z" fill="var(--ink)"/><circle cx="184" cy="40" r="15" fill="#2c2c2c"/></svg>
</section>
<section class="envelope env-front" aria-label="Envelope front">
  <div class="brand" style="left:12px;top:12px;font-size:9px"><span class="dot"></span><span class="brand-text">Tavrel<br><span style="font-size:5px">Security Services Ltd.</span></span></div>
  <p class="address" style="left:7px;top:55px;font-size:7px;line-height:1.2">Street Name, City Name<br>State Zipcode</p>
  <div class="watermark" role="img" aria-label="Faint company mark watermark" style="left:185px;top:40px;width:130px;height:130px;font-size:11px;background:#f3f3f3;color:#e6e6e6">Tavrel<br>Security</div>
  <p class="address" style="left:7px;top:150px;font-size:6.6px">www.tavrelsecurity.com</p>
  <svg class="band" viewBox="0 0 100 8" preserveAspectRatio="none" style="width:100%"><use href="#band"/></svg>
</section>

<!-- Business cards -->
<section class="card card-a" aria-label="Business card front">
  <div class="brand" style="left:40px;top:8px;font-size:7.5px"><span class="dot" style="width:8px;height:8px"></span><span class="brand-text">Tavrel<br><span style="font-size:4px">Security Services Ltd.</span></span></div>
  <p style="position:absolute;right:82px;top:45px;text-align:right;font-size:5px;line-height:1.3">Your Name<br><span style="font-size:3.8px">Title</span><br><span style="font-size:3.6px">Street Name, City Name<br>State Zip Code</span></p>
  <ul class="contact-list" style="left:64px;top:45px;font-size:3.8px;line-height:1.5">
    <li>555-310-4821</li><li>555-310-4867</li><li>info@tavrelsecurity.com</li><li>www.tavrelsecurity.com</li>
  </ul>
  <svg class="band" viewBox="0 0 100 8" preserveAspectRatio="none" style="width:100%;height:4px"><use href="#band"/></svg>
</section>
<section class="card card-b" aria-label="Business card back">
  <div class="brand" style="left:30px;top:18px;font-size:9px"><span class="dot"></span><span class="brand-text">Tavrel<br><span style="font-size:5px">Security Services Ltd.</span></span></div>
  <p style="position:absolute;left:0;right:0;top:58px;text-align:center;font-size:6px">www.tavrelsecurity.com</p>
</section>
<section class="card card-c" aria-label="Business card back, watermark variant">
  <div class="watermark" role="img" aria-label="Faint company mark watermark" style="left:40px;top:-4px;width:62px;height:62px;font-size:6px;background:#f2f2f2;color:#e4e4e4">Tavrel</div>
  <div class="brand" style="left:30px;top:44px;font-size:9px"><span class="dot"></span><span class="brand-text">Tavrel<br><span style="font-size:5px">Security Services Ltd.</span></span></div>
  <p style="position:absolute;left:0;right:0;top:66px;text-align:center;font-size:6px">www.tavrelsecurity.com</p>
</section>

<p class="option" style="left:111px">Option-1</p>
<p class="option" style="left:497px">Option-2</p>
</body>
</html>
```